Business card for law firm

Need business card for new law firm. Think confident, authoritative, conservative, but not stuffy or old-fashioned.

Contact Information for Business Card

Content for card - logo (uploaded), plus the following:

Paul Wexbury (larger font)
Managing Partner (larger font, but not as large as name)
Level 9, 41 Tansy Lane
Sydney NSW 2000
Main Tel 02 7346 2190
Direct Tel 02 6273 4415
Email paul@qvlegal.com.au
www.qvlegal.com.au

Letterhead design should include logo plus:
Level 9, 41 Tansy Lane
Sydney NSW 2000
Tel 02 6273 4415
www.qvlegal.com.au

```html
<!DOCTYPE html>
<html lang="en">
<head>
<meta charset="utf-8">
<title>Quayvale Legal – Business Card</title>
<link href="https://fonts.googleapis.com/css2?family=Open+Sans:wght@400;600;700&display=swap" rel="stylesheet">
<style>
  :root {
    --navy: #0a1f5c;
    --paper: #ffffff;
    --paper-shade: #ececec;
    --ink: #1a1a1a;
    --ink-soft: #4a4a4a;
    --backdrop: #3a3b3d;
  }
  * { box-sizing: border-box; margin: 0; padding: 0; }
  html, body {
    width: 1200px; height: 1000px; overflow: hidden;
    background: var(--backdrop);
    font-family: "Open Sans", Arial, sans-serif;
  }
  .stage { position: relative; width: 1200px; height: 1000px; }

  .card {
    position: absolute; left: 250px; width: 700px; height: 428px;
    overflow: hidden;
    box-shadow: 0 10px 28px rgba(0,0,0,0.45);
  }

  /* Front */
  .card-front {
    top: 56px;
    background: linear-gradient(160deg, var(--paper) 55%, var(--paper-shade) 100%);
  }
  .name-band {
    position: absolute; left: 210px; right: 0; top: 64px; height: 112px;
    background: var(--navy); color: var(--paper);
    text-align: right; padding: 0 22px 12px 0;
    display: flex; flex-direction: column; justify-content: flex-end;
    text-transform: uppercase;
  }
  .person-name { font-size: 25px; font-weight: 700; line-height: 1.15; }
  .person-title { font-size: 16px; font-weight: 700; line-height: 1.2; }

  .brand {
    position: absolute; left: 36px; top: 186px;
    display: flex; align-items: center; gap: 12px;
  }
  .brand-square { width: 26px; height: 26px; background: var(--navy); }
  .brand-name {
    font-size: 28px; font-weight: 600; color: var(--ink);
    letter-spacing: 2px; text-transform: uppercase; white-space: nowrap;
  }

  .contact-list {
    position: absolute; left: 36px; top: 246px; list-style: none;
    font-size: 16px; color: var(--ink-soft);
  }
  .contact-list li { display: flex; align-items: center; gap: 12px; height: 26px; }
  .contact-list svg { width: 16px; height: 16px; fill: var(--navy); flex: none; }

  .address {
    position: absolute; right: 34px; bottom: 30px;
    text-align: right; font-size: 20px; line-height: 1.3; color: var(--ink-soft);
    font-style: normal;
  }

  /* Back */
  .card-back {
    top: 520px;
    background: var(--navy);
  }
  .back-brand {
    position: absolute; inset: 0;
    display: flex; align-items: center; justify-content: center; gap: 14px;
  }
  .back-brand .brand-square { background: var(--paper); width: 30px; height: 30px; }
  .back-brand .brand-name { color: var(--paper); font-size: 34px; }
  .back-web {
    position: absolute; right: 60px; bottom: 48px;
    color: var(--paper); font-size: 16px; letter-spacing: 4px;
  }
</style>
</head>
<body>
<main class="stage">

  <section class="card card-front" aria-label="Business card front">
    <div class="name-band">
      <p class="person-name">Paul Wexbury</p>
      <p class="person-title">Managing Partner</p>
    </div>

    <div class="brand">
      <span class="brand-square"></span>
      <span class="brand-name">Quayvale Legal</span>
    </div>

    <ul class="contact-list">
      <li>
        <svg viewBox="0 0 16 16" aria-hidden="true"><path d="M2 5c0-2 2-3 6-3s6 1 6 3v1h-3V5H5v1H2zM4 7h8l2 7H2zM8 9a2 2 0 1 0 0 4 2 2 0 0 0 0-4z"/></svg>
        <span>02 7346 2190</span>
      </li>
      <li>
        <svg viewBox="0 0 16 16" aria-hidden="true"><path d="M4 1h8v14H4zM5.5 2.5v9h5v-9zM7 12.5h2v1.2H7z" fill-rule="evenodd"/></svg>
        <span>02 6273 4415</span>
      </li>
      <li>
        <svg viewBox="0 0 16 16" aria-hidden="true"><path d="M1 3h14v10H1zM1 3l7 6 7-6v1.5L8 10.5 1 4.5z"/></svg>
        <span>paul@qvlegal.com.au</span>
      </li>
    </ul>

    <address class="address">
      Level 9, 41 Tansy Lane<br>
      Sydney NSW 2000
    </address>
  </section>

  <section class="card card-back" aria-label="Business card back">
    <div class="back-brand">
      <span class="brand-square"></span>
      <span class="brand-name">Quayvale Legal</span>
    </div>
    <p class="back-web">www.qvlegal.com.au</p>
  </section>

</main>
</body>
</html>
```